Hardcore nerd needs to stand out in a sea of dull Defence business cards

Wombat Devices is a new Australian consulting engineering company that turns research and theory into practical systems. No evangelistic fluff, just mathematics and physics into electronic and optical circuits for consumer products, scientific research or Defence applications.

We already have a recognised logo (provided) which is often dark blue/black on a light background but we're open to other combinations. (Us engineers tend to have limited aesthetic imagination :)

Some of our recent products have included:
* Instrumentation for electrical testing,
* Radar jammers,
* GPS antenna design,
* Satellite tracking systems,
* High power lasers

We're open to both single and double-sided designs - happy to be convinced either way.

P.S. Another group is working on the web page, so - alas - our web site is currently of no use for images/ideas...

Target Market(s)

Engineering managers,
Scientists

Contact Information for Business Card

Dr Colin Marsh
R&D Engineer

colin@wombatdevicesco.com.au
0427 563 210

PO Box XXX (to be confirmed)
Banks ACT 2913
Australia

Font styles to use
Serif
Sans Serif

Colors

Designer to choose colors to be used in the design.

Requirements
Must have
• My contact details!
• I've had many (great) "bold and plain" designs submitted already, so feel free to be artistically creative :)
• Happy to take advice re fonts/colours/printability etc.
Nice to have
• I'm not sure if "lists" are more at home on a CV than a business card, but representative services include:
• Applied electromagnetics
• RF and high speed electronics
• Signal and image processing
• Electro-optical and laser systems
• Concept-to-prototype design services
• If you're considering double sided cards, then often measuring/alignment grids/rulers feature on the back of similar cards.
• e.g. https://www.lumoptix-example.com/newgrouppage9.cfm?objectgroup_id=4815
• https://www.lumoptix-example.com/newgrouppage9.cfm?objectgroup_ID=4817
• ..or even a "Smith chart" (google will return lots)
• Generic images to represent a capability might work - googling images associated with keyword for each of these areas might help:
• - "passive radar", "phased array", "fdtd", "vircator"
• RF and high speed electronic design
• - "smith chart", "microstrip circuits", "dimensioned drawing", "electronic schematic"
• - "dft", "iir filter"
• - "optical cavity". "laser energy level diagram"
• Background/watermarked images outlines/wireframes/schematics would probably look OK.
Should not have
• If a list of projects/services is provided, it is important not to make the client feel that this is "all" the company can do. Engineering design is a creative discipline (like graphics :)
• Please, no stock "military" snaps like planes, missiles, etc!

```html
<!DOCTYPE html>
<html lang="en">
<head>
<meta charset="utf-8">
<title>Wombat Devices – Business Card</title>
<link href="https://fonts.googleapis.com/css2?family=Roboto:wght@400;500;700&display=swap" rel="stylesheet">
<style>
  :root {
    --page-bg: #e4e4e4;
    --card-white: #ffffff;
    --brand-navy: #0a3478;
    --navy-top: #022c70;
    --navy-bottom: #00205e;
    --text-grey: #4a4a4a;
    --title-grey: #9a9a9a;
    --white: #ffffff;
  }
  * { margin: 0; padding: 0; box-sizing: border-box; }
  html, body {
    width: 1200px; height: 1200px; overflow: hidden;
    background: var(--page-bg);
    font-family: "Roboto", Arial, sans-serif;
  }
  .sheet {
    width: 1200px; height: 1200px;
    display: flex; flex-direction: column; align-items: center; justify-content: center;
    gap: 72px;
  }
  .card {
    position: relative;
    width: 900px; height: 514px;
    border-radius: 26px;
    overflow: hidden;
  }
  .card--front { background: var(--card-white); }
  .card--back {
    background: linear-gradient(180deg, var(--navy-top), var(--navy-bottom));
    color: var(--white);
  }
  .person {
    position: absolute; top: 44px; right: 53px; text-align: right;
  }
  .person__name {
    font-size: 29px; font-weight: 700; color: var(--brand-navy); letter-spacing: 0.2px;
  }
  .person__title {
    font-size: 21px; color: var(--title-grey); margin-top: 2px;
  }
  .contact {
    position: absolute; left: 55px; top: 297px;
    font-size: 20px; color: var(--text-grey); line-height: 26px;
  }
  .contact__address { margin-bottom: 11px; }
  .contact__line { display: flex; align-items: center; gap: 10px; }
  .contact__line svg { width: 17px; height: 17px; flex: none; fill: var(--brand-navy); }
  .brand {
    position: absolute; left: 0; right: 0; top: 196px;
    display: flex; align-items: center; justify-content: center; gap: 22px;
  }
  .brand__dot {
    width: 96px; height: 96px; border-radius: 50%; background: var(--white);
  }
  .brand__name {
    font-size: 50px; font-weight: 700; letter-spacing: 2px; color: var(--white);
  }
  .services {
    position: absolute; left: 0; right: 0; top: 402px;
    text-align: center; font-size: 20px; line-height: 26px;
  }
</style>
</head>
<body>
<main class="sheet">
  <section class="card card--front" aria-label="Card front">
    <div class="person">
      <div class="person__name">Dr Colin Marsh</div>
      <div class="person__title">R&amp;D Engineer</div>
    </div>
    <div class="contact">
      <div class="contact__address">PO Box XXX<br>Banks ACT 2913<br>Australia</div>
      <div class="contact__line">
        <svg viewBox="0 0 24 24" aria-hidden="true"><path d="M6.6 10.8c1.4 2.8 3.8 5.1 6.6 6.6l2.2-2.2c.3-.3.7-.4 1-.2 1.1.4 2.3.6 3.6.6.6 0 1 .4 1 1V20c0 .6-.4 1-1 1C10.6 21 3 13.4 3 4c0-.6.4-1 1-1h3.5c.6 0 1 .4 1 1 0 1.3.2 2.5.6 3.6.1.3 0 .7-.2 1z"/></svg>
        <span>0427 563 210</span>
      </div>
      <div class="contact__line">
        <svg viewBox="0 0 24 24" aria-hidden="true"><path d="M3 6h18v12H3z M4 7l8 6 8-6" fill="none" stroke="#0a3478" stroke-width="2"/><path d="M3 6h18v2l-9 6-9-6z"/></svg>
        <span>colin@wombatdevicesco.com.au</span>
      </div>
      <div class="contact__line">
        <svg viewBox="0 0 24 24" aria-hidden="true"><circle cx="12" cy="12" r="9.5" fill="none" stroke="#0a3478" stroke-width="2.5"/><path d="M8 6c2 1 1 3 3 4s0 3 2 4 1 3 0 5c-3 0-7-3-7-7 0-2 1-4 2-6zM15 5c1 1 2 2 1 3s2 2 3 2c0-2-2-4-4-5z"/></svg>
        <span>www.wombatdevicesco.com.au</span>
      </div>
    </div>
  </section>

  <section class="card card--back" aria-label="Card back">
    <div class="brand">
      <span class="brand__dot" aria-hidden="true"></span>
      <span class="brand__name">Wombat Devices</span>
    </div>
    <div class="services">
      <p>Applied electromagnetics • RF &amp; high speed electronics</p>
      <p>Signal &amp; image processing • Electro-optical &amp; laser systems</p>
      <p>Concept-to-prototype design services</p>
    </div>
  </section>
</main>
</body>
</html>
```